Brookmere - a website to encourage people to spend time in nature

I have a squarespace site with some content on it but the squarespace template doesn't completely suit my needs, I keep fiddling with the template but actually I need some professional help to get it looking the way I want and with the right 'mood'.
The website is for "Brookmere" - it will be a blog where I write about the importance of nature for good health. I also want to use the website to market services such as outdoor coaching, retreats and walking workshops.
This has been in my head for a LONG time and I currently only use instagram for micro-blogs but it's time for me to get this moving. I've previously engaged other designers on branding for it but they just didn't get it quite the way that I wanted it and I wasn't completely happy with the results. It's been a process for me as to what I want but in the meantime I just didn't come back to the design aspect of it now. I'm looking for a designer who understands the purpose of the website, the ethos and can help me realise this into a design that's clean, clear and simple.

Please note that I have a domain (brookmere.org) and a lot of content drafted on squarespace already. I have published it with password protection - password is brookmere2020 - it still has some of the original template on it, but does have some content. Don't take it as anything to follow in particular, i am looking for fresh eyes and fresh ideas.

Target Market(s)

There are three main groups that I want to target - people who are suffering from stress and anxiety, people who treat them and parents who want to get their kids outside (thereby preventing stress and anxiety)

Contact Information for Business Card

Helen Corbett
Brookmere
Telephone +44 7942 310587
brookmere@mailpost.net

Logo Text

Brookmere - if that. I have an idea that the logo should have a leaf on it somewhere, or maybe just be a leaf.

Coding

Coded - Design and coding required

Number of Pages Required

5+ page

Font styles to use
Serif
Sans Serif

Colors
add136
33b8a4
34a6d7
3377b5

Requirements
Must have
• Space for lots of images. The ability for me to edit the pages if I need to. Be user friendly. Look beautiful.
• For an idea of the images I use and the content I'm interested in writing about have a look at @brookmere on instagram.
• That pop up about cookies so I am complying with data laws.
Should not have
• Must not be too 'busy' I'd like to avoid too much movement.

```html
<!DOCTYPE html>
<html lang="en">
<head>
<meta charset="utf-8">
<title>Brookmere</title>
<link rel="stylesheet" href="https://fonts.googleapis.com/css2?family=Merienda:wght@400;700&family=Poppins:wght@300;400;500;600&family=Lora:wght@400&display=swap">
<style>
:root{
  --mint:#d3ece7;
  --mint-bar:#9fdcd0;
  --paper:#f6f6f6;
  --contact-bg:#f1f5f4;
  --blue:#3377b5;
  --blue-soft:#5b8ec9;
  --ink:#222;
  --grey:#777;
  --white:#fff;
  --dark:#2a2a2a;
}
*{margin:0;padding:0;box-sizing:border-box}
html,body{width:1200px;height:4446px;overflow:hidden}
body{position:relative;background:var(--paper);font-family:'Poppins',sans-serif;color:var(--ink)}
.abs{position:absolute}
.center{left:0;width:100%;text-align:center}
.display{font-family:'Merienda',cursive}
.photo{position:absolute}
.btn{position:absolute;background:var(--blue);color:var(--white);border-radius:5px;font-family:'Merienda',cursive;font-weight:700;font-size:13px;letter-spacing:2px;display:flex;align-items:center;justify-content:center;box-shadow:0 3px 6px rgba(0,0,0,.2)}
.btn--light{background:var(--white);color:var(--blue)}
.field{position:absolute;background:var(--white);border:2px solid #e2e2e2;border-radius:6px;font-size:12px;color:#bbb;padding-left:40px;display:flex;align-items:center}
.dot{display:inline-block;width:12px;height:12px;border-radius:50%;background:currentColor;vertical-align:middle;margin-right:10px}

/* top bar */
.topbar{left:0;top:0;width:1200px;height:35px;background:var(--mint-bar);font-size:13px;color:#5c8f87}
.topbar__social{left:60px;top:10px;color:#2c4f49}
.topbar__nav{left:446px;top:8px;display:flex;gap:38px}
.topbar__nav a{color:#5c8f87;text-decoration:none}
.topbar__nav .is-active{text-decoration:underline}
.topbar__search{left:1078px;top:9px;font-size:10px;color:#2c4f49;display:flex;align-items:center;gap:8px}

/* header */
.site-title{top:58px;font-size:54px;font-weight:700;letter-spacing:2px}
.tagline{top:135px;font-size:13px;color:var(--grey);letter-spacing:.5px}

/* hero */
.hero{left:0;top:221px;width:1200px;height:1086px;background:var(--mint)}
.card{position:absolute;background:var(--white)}
.welcome__avatar{left:830px;top:331px;width:184px;height:184px;border-radius:50%;border:5px solid var(--white);background:linear-gradient(160deg,#e8ecef,#a8b0b8)}
.welcome__title{left:703px;width:437px;top:553px;font-size:15px;font-weight:700;letter-spacing:1px}
.welcome__text{left:780px;width:283px;top:584px;font-size:13px;line-height:22px;color:#555;letter-spacing:.5px}
.welcome__social{left:878px;top:643px;color:#222}
.subscribe__title{left:703px;width:437px;top:748px;font-size:38px;font-weight:700;letter-spacing:5px}
.subscribe__sub{left:703px;width:437px;top:810px;font-size:13px;color:var(--blue);letter-spacing:3px;font-weight:700}
.more-blogs{left:703px;top:1045px;width:437px;height:145px;background:var(--blue);color:var(--white);font-size:36px;letter-spacing:5px;display:flex;align-items:center;justify-content:center}

/* about */
.section-title{font-size:54px;font-weight:700;letter-spacing:1px}
.origin{left:97px;top:1525px;width:502px;height:504px;border-radius:6px;background:linear-gradient(180deg,#5b8ec9 0%,#5a8fc6 60%,#6f98c4 100%)}
.origin__title{left:150px;top:1635px;font-size:28px;color:var(--white);font-weight:700}
.origin__lead{left:150px;top:1688px;font-size:16px;color:var(--white);letter-spacing:2px}
.origin__text{left:150px;top:1717px;width:400px;font-size:13px;line-height:23px;color:#e9f0f8;letter-spacing:1px}
.feature__title{font-size:28px;font-weight:700}
.feature__text{width:280px;font-size:13px;line-height:23px;color:var(--grey);letter-spacing:1.5px}

/* blogs */
.blogs{left:0;top:2143px;width:1200px;height:1737px;background:var(--mint)}
.blogs__sub{top:2322px;font-size:28px;color:var(--blue);font-style:italic}
.blogs__date{top:2384px;font-size:19px;color:#666}
.blogs__rule{left:585px;top:2430px;width:30px;height:2px;background:#444}
.post{position:absolute;width:323px;text-align:center}
.post__img{width:323px;height:323px}
.post__title{font-family:'Lora',serif;font-size:26px;line-height:34px;margin-top:60px;color:#333;letter-spacing:1px;height:68px}
.post__text{font-size:14px;line-height:26px;color:#666;margin:22px auto 0;width:290px}
.post__more{font-family:'Lora',serif;font-size:13px;color:var(--blue);margin-top:22px;display:flex;align-items:center;justify-content:center;gap:10px}

/* contact */
.contact{left:0;top:3880px;width:1200px;height:282px;background:var(--contact-bg)}
.contact__sub{top:4012px;font-size:13px;color:#888;letter-spacing:2px}
.footer{left:0;top:4162px;width:1200px;height:219px;background:var(--blue)}
.footer__title{left:64px;top:4228px;font-size:38px;font-weight:700;letter-spacing:5px;color:#1d2a36}
.footer__sub{left:64px;top:4282px;font-size:13px;font-weight:700;letter-spacing:3px;color:#1d2a36}
.footer__social{left:1027px;top:4330px;color:var(--white)}
.copyright{left:0;top:4381px;width:1200px;height:65px;background:var(--dark);color:var(--white);font-size:13px;display:flex;align-items:center;justify-content:center;gap:8px;letter-spacing:.5px}
</style>
</head>
<body>

<header>
  <div class="abs topbar"></div>
  <div class="abs topbar__social"><span class="dot"></span><span class="dot"></span><span class="dot"></span>
    <svg width="13" height="10" viewBox="0 0 13 10" style="vertical-align:middle"><rect x=".5" y=".5" width="12" height="9" fill="none" stroke="currentColor"/><path d="M.5 .5l6 5 6-5" fill="none" stroke="currentColor"/></svg>
  </div>
  <nav class="abs topbar__nav"><a class="is-active" href="#">Home</a><a href="#">About us</a><a href="#">Blogs</a><a href="#">Contact</a></nav>
  <div class="abs topbar__search">search..
    <svg width="12" height="12" viewBox="0 0 12 12"><circle cx="5" cy="5" r="3.8" fill="none" stroke="currentColor" stroke-width="1.6"/><path d="M8 8l3 3" stroke="currentColor" stroke-width="1.6"/></svg>
  </div>
  <h1 class="abs center display site-title">Brookmere</h1>
  <p class="abs center tagline">The practice of spending time in nature to feel better.</p>
</header>

<section>
  <div class="abs hero"></div>
  <div class="photo" role="img" aria-label="Smiling woman with a bicycle among pink blossom" style="left:60px;top:221px;width:612px;height:608px;background:linear-gradient(135deg,#c9a98a 0%,#b98a5f 45%,#e9d9c5 70%,#d6a8b4 100%)"></div>
  <div class="photo" role="img" aria-label="Hammock between palm trees at sunset" style="left:60px;top:857px;width:187px;height:335px;background:linear-gradient(180deg,#8fb0c8,#b89978 70%,#5a4a3a)"></div>
  <div class="photo" role="img" aria-label="Two children walking down a sunny lane" style="left:273px;top:857px;width:186px;height:335px;background:linear-gradient(180deg,#e6cfa6,#b29373 60%,#8c8373)"></div>
  <div class="photo" role="img" aria-label="Green tree tunnel over a path" style="left:485px;top:857px;width:187px;height:335px;background:radial-gradient(circle at 50% 75%,#c9e08a,#4f9a2e 40%,#2a6a1c)"></div>

  <div class="card" style="left:703px;top:221px;width:437px;height:477px"></div>
  <div class="photo" role="img" aria-label="Stacked pebbles by a blue sea" style="left:703px;top:221px;width:437px;height:219px;background:linear-gradient(180deg,#1f5fa8,#4d8fcf 70%,#a98d6c)"></div>
  <div class="photo welcome__avatar" role="img" aria-label="Portrait of the author"></div>
  <h2 class="abs display welcome__title" style="text-align:center">Welcome to Brookmere.</h2>
  <p class="abs welcome__text" style="text-align:center">I document the relationship between nature and better health.</p>
  <div class="abs welcome__social"><span class="dot"></span><span class="dot" style="margin-left:20px"></span><span class="dot" style="margin-left:20px"></span></div>

  <div class="card" style="left:703px;top:727px;width:437px;height:288px"></div>
  <h2 class="abs display subscribe__title" style="text-align:center">Subscribe</h2>
  <p class="abs display subscribe__sub" style="text-align:center">Stay Connected</p>
  <div class="field" style="left:736px;top:862px;width:387px;height:41px">Email</div>
  <div class="btn" style="left:860px;top:931px;width:123px;height:41px">Sign up</div>

  <div class="abs display more-blogs">More Blogs</div>
</section>

<section>
  <h2 class="abs center display section-title" style="top:1395px">About Us</h2>
  <div class="abs origin" role="img" aria-label="Person sitting by the sea under a blue overlay"></div>
  <h3 class="abs display origin__title">Origin Story</h3>
  <p class="abs origin__lead">In The Beginning...</p>
  <p class="abs origin__text">Brookmere Was Founded In 2017 By Me, Helen Corbett, &nbsp;A Recovering Lawyer/Corporate Junkie. I Had Spent Most Of The Previous Fifteen Years In Offices In London And For Many Of Those Years I Had Been Sedantry, Stressed And Ill-At-Ease With Myself.</p>
  <div class="btn btn--light" style="left:150px;top:1876px;width:144px;height:40px">Read More</div>

  <div class="photo" role="img" aria-label="Pink cherry blossom" style="left:620px;top:1525px;width:180px;height:245px;background:linear-gradient(135deg,#f4b7c8,#d9587e 50%,#f7d2dc)"></div>
  <div class="photo" role="img" aria-label="Dog on a beach under a blue sky" style="left:620px;top:1784px;width:180px;height:245px;background:linear-gradient(180deg,#4f86c9,#bcd3e6 50%,#8b7b68)"></div>

  <h3 class="abs display feature__title" style="left:827px;top:1568px">What We Do</h3>
  <p class="abs feature__text" style="left:827px;top:1620px">We Do Some Things That Will Help You Get Back To Nature.</p>
  <div class="btn" style="left:827px;top:1686px;width:134px;height:40px">Read More</div>
  <h3 class="abs display feature__title" style="left:829px;top:1803px">Partners</h3>
  <p class="abs feature__text" style="left:829px;top:1853px">We Believe We Work Better When We Work Together. &nbsp;We Are Proud To Work Together With These Organisations.</p>
  <div class="btn" style="left:827px;top:1968px;width:136px;height:40px">Read More</div>
</section>

<section>
  <div class="abs blogs"></div>
  <h2 class="abs center display section-title" style="top:2232px">Blogs</h2>
  <p class="abs center display blogs__sub">Good for you. Good for the plannet</p>
  <p class="abs center blogs__date">Feb 14</p>
  <div class="abs blogs__rule"></div>

  <article class="post" style="left:71px;top:2506px">
    <div class="post__img" role="img" aria-label="City park in autumn beneath a rainbow" style="background:linear-gradient(180deg,#a9a59c,#c8a55a 50%,#5b6a2e)"></div>
    <h3 class="post__title">Why being outside is good for the planet</h3>
    <p class="post__text">The focus of Brookmere is on people. Making people feel better through time spent in nature...</p>
    <p class="post__more">Read More <svg width="16" height="8" viewBox="0 0 16 8"><path d="M0 4h14M11 1l3 3-3 3" fill="none" stroke="currentColor"/></svg></p>
  </article>
  <article class="post" style="left:435px;top:2506px">
    <div class="post__img" role="img" aria-label="Sun shining through bare winter trees" style="background:radial-gradient(circle at 55% 62%,#f4f0e4,#6a8bd0 25%,#1d3f8e 60%,#1b2236)"></div>
    <h3 class="post__title">Thank Rupert Vance copy</h3>
    <p class="post__text">I had had a lot of thoughts about creating Brookmere for a while. No real direction or goal...</p>
    <p class="post__more">Read More <svg width="16" height="8" viewBox="0 0 16 8"><path d="M0 4h14M11 1l3 3-3 3" fill="none" stroke="currentColor"/></svg></p>
  </article>
  <article class="post" style="left:800px;top:2506px">
    <div class="post__img" role="img" aria-label="Bird nest in an old stone wall" style="background:linear-gradient(135deg,#d6d6d4,#a9a7a2 50%,#cfcecb)"></div>
    <h3 class="post__title">Notes From the Nest</h3>
    <p class="post__text">Growing up in this part of the world, I had the best playground. There are plenty of grainy...</p>
    <p class="post__more">Read More <svg width="16" height="8" viewBox="0 0 16 8"><path d="M0 4h14M11 1l3 3-3 3" fill="none" stroke="currentColor"/></svg></p>
  </article>

  <article class="post" style="left:71px;top:3171px">
    <div class="post__img" role="img" aria-label="Red pool terrace with parasols under a tree" style="background:linear-gradient(180deg,#eef2f2 30%,#d33a36 70%,#9c1f1f)"></div>
    <h3 class="post__title">In The Beginning There Was Vance</h3>
    <p class="post__text">The focus of Brookmere is on people. Making people feel better through time spent in nature...</p>
    <p class="post__more">Read More</p>
  </article>
  <article class="post" style="left:435px;top:3171px">
    <div class="post__img" role="img" aria-label="Cloudy sky" style="background:linear-gradient(160deg,#8fa2b8,#e6e7e6 45%,#95a6ba)"></div>
    <h3 class="post__title">Skytime Over Screentime</h3>
    <p class="post__text">I had had a lot of thoughts about creating Brookmere for a while. No real direction or goal...</p>
    <p class="post__more">Read More</p>
  </article>
  <article class="post" style="left:800px;top:3171px">
    <div class="post__img" role="img" aria-label="Child in a meadow of wildflowers" style="background:linear-gradient(180deg,#c9d8e6,#8a9a6a 45%,#4e6a2c)"></div>
    <h3 class="post__title">On the Verge</h3>
    <p class="post__text">Growing up in this part of the world, I had the best playground. There are plenty of grainy...</p>
    <p class="post__more">Read More</p>
  </article>
</section>

<section>
  <div class="abs contact"></div>
  <h2 class="abs center display section-title" style="top:3921px">Contact us</h2>
  <p class="abs center contact__sub">Email Me For Press/Media Inquiries And Other Collaborations.</p>
  <div class="btn" style="left:389px;top:4066px;width:424px;height:39px;letter-spacing:1px">hello@brookmere.org</div>
</section>

<footer>
  <div class="abs footer"></div>
  <h2 class="abs display footer__title">Subscribe</h2>
  <p class="abs display footer__sub">Stay Connected</p>
  <div class="field" style="left:297px;top:4252px;width:383px;height:40px;border:none;padding-left:28px">Email</div>
  <div class="btn" style="left:694px;top:4252px;width:123px;height:40px">Sign up</div>
  <div class="abs footer__social"><span class="dot" style="width:14px;height:14px;margin-right:18px"></span><span class="dot" style="width:14px;height:14px;margin-right:18px"></span><span class="dot" style="width:14px;height:14px;margin-right:18px"></span>
    <svg width="16" height="12" viewBox="0 0 16 12" style="vertical-align:middle"><rect x=".5" y=".5" width="15" height="11" fill="none" stroke="currentColor"/><path d="M.5 .5l7.5 6 7.5-6" fill="none" stroke="currentColor"/></svg>
  </div>
  <div class="abs copyright">
    <svg width="16" height="16" viewBox="0 0 16 16"><circle cx="8" cy="8" r="7" fill="none" stroke="currentColor" stroke-width="1.3"/><path d="M10.5 6a3 3 0 1 0 0 4" fill="none" stroke="currentColor" stroke-width="1.3"/></svg>
    Copyright@Brookmere2019
  </div>
</footer>

</body>
</html>
```